Medical Device Company needs website

We are a start-up medical device company looking to sell boot (foot) and brace (ankle) products on Shopify. We are still working on the name but you can use Tavrix as a placeholder- no logo yet)

Website information:
- Look: modern/tech with clean lines and symmetry.
- Colors: teal, white, black, and greys.
- Headers: home, shop, about us, help, blog
- Icons (upper right): search, my account and shopping cart
-place to sign up for newsletter

```html
<!DOCTYPE html>
<html lang="en">
<head>
<meta charset="utf-8">
<title>Tavrix – Blog &amp; Newsletter</title>
<link href="https://fonts.googleapis.com/css2?family=Jost:wght@400;500&display=swap" rel="stylesheet">
<style>
:root{
  --page:#f5f5f5;
  --white:#ffffff;
  --ink:#1d1d1f;
  --navy:#1b2350;
  --muted:#7a7a7a;
  --date:#9a9a9a;
  --teal:#0f8a86;
  --footer:#f3f3f3;
  --black:#000000;
}
*{margin:0;padding:0;box-sizing:border-box}
html,body{width:1200px;height:1200px;overflow:hidden;background:var(--page);font-family:"Jost",sans-serif;color:var(--ink)}
.canvas{position:relative;width:1200px;height:1200px}
.blog{position:absolute;top:83px;left:0;width:1200px;height:586px;background:var(--white)}
.blog-title{position:absolute;top:42px;width:100%;text-align:center;font-size:25px;font-weight:500;letter-spacing:1px}
.blog-intro{position:absolute;top:88px;width:100%;text-align:center;font-size:11px;color:#555}
.post{position:absolute;top:139px;width:270px;text-align:center}
.post-photo{width:225px;height:225px;border-radius:50%;margin:0 auto}
.post-title{margin-top:26px;font-size:16px;font-weight:500;color:var(--navy)}
.post-date{margin-top:5px;font-size:7px;letter-spacing:1.5px;color:var(--date)}
.post-rule{width:44px;height:1px;background:var(--ink);margin:10px auto 0}
.post-body{margin-top:12px;font-size:9.5px;line-height:17.5px;color:var(--muted)}
.newsletter{position:absolute;top:669px;left:0;width:1200px;height:202px;background:linear-gradient(90deg,#3a3a2c 0%,#4a3a30 35%,#3a302c 60%,#4d4740 100%)}
.nl-icon{position:absolute;left:244px;top:77px}
.nl-divider{position:absolute;left:300px;top:68px;width:1px;height:57px;background:var(--white)}
.nl-heading{position:absolute;left:316px;top:70px;font-size:15px;letter-spacing:5px;color:var(--teal)}
.nl-text{position:absolute;left:316px;top:95px;font-size:12px;line-height:15px;color:var(--white);width:260px}
.nl-input{position:absolute;left:619px;top:83px;width:232px;height:38px;background:var(--white);font-size:8px;color:#555;padding-left:15px;line-height:38px;font-weight:500}
.nl-submit{position:absolute;left:851px;top:83px;width:96px;height:38px;background:var(--black);color:var(--white);font-size:7.5px;letter-spacing:2px;text-align:center;line-height:38px;font-weight:500}
.footer{position:absolute;top:871px;left:0;width:1200px;height:245px;background:var(--footer)}
.brand{position:absolute;left:159px;top:35px;display:flex;align-items:center;gap:8px;font-size:26px;font-weight:500;color:var(--ink)}
.brand-mark{width:22px;height:22px;background:var(--teal)}
.about{position:absolute;left:159px;top:89px;width:340px;font-size:8.7px;line-height:13px}
.social{position:absolute;left:162px;top:143px;display:flex;gap:14px}
.social span{width:10px;height:10px;border-radius:50%;background:var(--ink)}
.col{position:absolute;top:32px}
.col h4{font-size:11px;font-weight:500}
.col .rule{width:19px;height:1px;background:var(--ink);margin:10px 0 12px}
.col a{display:block;font-size:9.4px;color:var(--ink);text-decoration:none;height:21.3px}
.bottom{position:absolute;top:195px;left:0;width:1200px;border-top:1px solid #e8e8e8;height:50px}
.copyright{position:absolute;left:159px;top:20px;font-size:8.7px}
.copyright em{font-style:normal;color:#666}
.cards{position:absolute;left:922px;top:17px;display:flex;gap:5px}
.cards span{width:26px;height:16px;border-radius:1px}
</style>
</head>
<body>
<div class="canvas">
  <section class="blog">
    <h2 class="blog-title">OUR BLOG POSTS</h2>
    <p class="blog-intro">A collection of stories about the Boots and Acnkes supplies we admire.</p>

    <article class="post" style="left:165px">
      <div class="post-photo" role="img" aria-label="Photo of feet in cream socks resting by a window" style="background:radial-gradient(circle at 60% 55%,#c9bf9e,#7d8590 55%,#3b4a66)"></div>
      <h3 class="post-title">Per Ultricies Augue Primis</h3>
      <p class="post-date">OCTOBER 19, 2024</p>
      <div class="post-rule"></div>
      <p class="post-body">Lorem ipsum dolor sit amet, consectetuer adipiscing elit. Aenean commodo ligula eget dolor. Aenean massa. Cum sociis natoque penatibus et magnis dis parturient montes, nascetur...</p>
    </article>

    <article class="post" style="left:465px">
      <div class="post-photo" role="img" aria-label="Photo of a clinician examining a patient's foot" style="background:radial-gradient(circle at 55% 45%,#c8ccd0,#8c9298 50%,#1f4f7a)"></div>
      <h3 class="post-title">Consectetuer Tempor Donec</h3>
      <p class="post-date">OCTOBER 19, 2024</p>
      <div class="post-rule"></div>
      <p class="post-body">Lorem ipsum dolor sit amet, consectetuer adipiscing elit. Aenean commodo ligula eget dolor. Aenean massa. Cum sociis natoque penatibus et magnis dis parturient montes, nascetur...</p>
    </article>

    <article class="post" style="left:765px">
      <div class="post-photo" role="img" aria-label="Photo of legs in rust trousers and black rubber boots on a path" style="background:radial-gradient(circle at 50% 40%,#6e3a22,#3a2f28 55%,#4b4236)"></div>
      <h3 class="post-title">Porta Rhoncus Facilisi Rutrum</h3>
      <p class="post-date">OCTOBER 19, 2024</p>
      <div class="post-rule"></div>
      <p class="post-body">Lorem ipsum dolor sit amet, consectetuer adipiscing elit. Aenean commodo ligula eget dolor. Aenean massa. Cum sociis natoque penatibus et magnis dis parturient montes, nascetur...</p>
    </article>
  </section>

  <section class="newsletter" role="img" aria-label="Darkened photo of rubber boots on a leafy path behind the newsletter signup">
    <svg class="nl-icon" width="40" height="40" viewBox="0 0 40 40" fill="none" stroke="#fff" stroke-width="2">
      <path d="M2 16 L20 3 L38 16 V38 H2 Z"/>
      <path d="M7 20 V8 H33 V20"/>
      <path d="M12 13 H28 M12 17 H28"/>
      <path d="M2 16 L20 28 L38 16 M2 38 L16 26 M38 38 L24 26"/>
    </svg>
    <div class="nl-divider"></div>
    <h3 class="nl-heading">OUR NEWSLETTER!</h3>
    <p class="nl-text">It only takes a second to be the first to find out about our latest news</p>
    <div class="nl-input">Your email address...</div>
    <div class="nl-submit">SUBMIT</div>
  </section>

  <footer class="footer">
    <div class="brand"><span class="brand-mark"></span>Tavrix</div>
    <p class="about">Lorem ipsum dolor sit amet, consectetur adipiscing elit, sed do eiusmod tempor incididunt ut labore et dolore magna aliqua. Ut enim ad minim veniam, quis nostrud exercitation ullamco laboris nisi ut aliquip ex ea commodo consequat.</p>
    <div class="social"><span></span><span></span><span></span><span></span></div>

    <nav class="col" style="left:534px">
      <h4>Help &amp; Information</h4><div class="rule"></div>
      <a>About Us</a><a>Return Policy</a><a>Privacy Policy</a><a>Wholesale Policy</a>
    </nav>
    <nav class="col" style="left:735px">
      <h4>Quick Links</h4><div class="rule"></div>
      <a>Help</a><a>Wishlist</a><a>Blog Posts</a><a>Contact US</a>
    </nav>
    <nav class="col" style="left:909px">
      <h4>Categories</h4><div class="rule"></div>
      <a>Boots</a><a>Ankles</a>
    </nav>

    <div class="bottom">
      <p class="copyright">© Copyright 2024 | Tavrix Medical By <em>Corvell Studio</em>.</p>
      <div class="cards">
        <span style="background:#fff;border:1px solid #ddd"></span>
        <span style="background:#0a4d9c"></span>
        <span style="background:#0b8a5a"></span>
        <span style="background:#2b4ea2"></span>
      </div>
    </div>
  </footer>
</div>
</body>
</html>
```